Design Book Cover for PhD Thesis on Cryptanalysis

I need a book cover design (front, back & spine) for my PhD thesis called "Lanterns over Quiet Harbors and Orchards".
Author: Tomas Brielink
Keywords: cryptanalysis, digital fingerprint, digital signature, digital certificate, collision of fingerprint/signature, bit-difference.
The finished book will have dimensions 17cm by 24cm by ?cm.
The (flat-)spine thickness is yet unknown, but will probably be about 1cm.
The cover design thus needs from left-to-right:
- a back of 17cm by 24cm
- in between a spine of about 1cm by 24cm
- a front of 17cm by 24cm
Around this design a 3mm bleeding/cutoff edge is needed
(leading to a total height of 24.6 cm and total width of 35.6cm).
The spine-fold is located 7mm from the spine on the front and back cover,
so the title etc. should be removed at least 1cm from the spine.
Below I will provide a description of my biggest results in my thesis and try to give some idea of the techniques used, which may help you for inspiration.
As you will read below, cryptanalysis comes close to "hacking".
However, cryptanalysis involves much more mathematics, and our goal is to provide recommendations which cryptographic standards are (un)safe to use.
So I would prefer a cover design that generally "feels" more as cryptanalysis than "hacking".
The biggest result in my thesis is the following.
Secure websites are secured using digital certificates.
These digital certificates contain the web domain name and the server's public-key and are digitally signed by a Certificate Authority (a company/government that only signs if the public-key really belongs to the owner of the web domain).
Only a few hundred Certification Authorities are trusted in web browsers and these are publically available.
Any digital certificate signed by such a Certification Authority is considered legitimate.
To fake a secure website you thus have to get a certificate containing your public-key in combination with the target domain name signed by a Certification Authority.
Our team was able to construct a rogue sub-Certification Authority, i.e.,
a Certification Authority that is authorized by one of the publicly known Certification Authorities.
Using our rogue Certification Authority we can thus create digital certificates at will for any secure website containing our public-key.
More detailed information is available at
http://www.kol.vrmq.nl/tinselgrove/blue-ox/
An idea of the techniques in my thesis:
I look at the internal computation of a digital signature for a certificate at bit-level and compare two such computations.
A difference between two certificates will lead to differences between the two internal computations of their digital signatures and finally to two different signatures.
However, we actively adapt the certificates to control the flow of these internal differences until we find two different certificates that actually result in the same digital signature, this is called a _collision_.
Evidently, my thesis is very technical and I have tried here to provide a short description.
You can always contact me for questions and/or more detailed explanations.
Reason: Almost all designs focus on the very general topic of digital security (digital fingerprint, etc).
I am looking more for a design that reflects more on the topic of the thesis: attacks on hash functions.
Several ideas have already been given in the brief and discussion.
Since the old deadline is already tomorrow, I am extend it.

```html
<!DOCTYPE html>
<html lang="en">
<head>
<meta charset="utf-8">
<title>Lanterns over Quiet Harbors and Orchards — Cover</title>
<link href="https://fonts.googleapis.com/css2?family=Encode+Sans+Condensed:wght@300;400&display=swap" rel="stylesheet">
<style>
  :root {
    --ground: #4a4a4a;
    --ink-light: #f0ecd8;
    --rule-grey: #b9b7ad;
    --gold: #a8935a;
    --gold-line: #c9a93a;
    --yellow: #e8c94a;
  }
  html, body {
    margin: 0;
    padding: 0;
    overflow: hidden;
    background: var(--ground);
  }
  .cover {
    display: block;
    width: 1200px;
    height: 828px;
    background: var(--ground);
    font-family: "Encode Sans Condensed", "Arial Narrow", sans-serif;
    font-weight: 300;
  }
  .rule-grey { stroke: var(--rule-grey); stroke-width: 0.8; fill: none; }
  .rule-gold { stroke: var(--gold-line); stroke-width: 0.9; fill: none; }
  .marker-outline { stroke: var(--ink-light); stroke-width: 1.1; fill: none; }
  .marker-solid { fill: var(--gold); stroke: none; }
  .front-title { fill: var(--ink-light); font-size: 20px; }
  .front-author { fill: var(--ink-light); font-size: 20px; }
  .back-author { fill: var(--ink-light); font-size: 11.5px; }
  .spine-author { fill: var(--ink-light); font-size: 11.5px; }
  .spine-title { fill: var(--yellow); font-size: 11.5px; }
  .band-title { fill: var(--yellow); font-size: 11.5px; }
  .imprint { fill: var(--gold); font-size: 11px; font-weight: 400; }
  .imprint-small { fill: var(--gold); font-size: 8px; font-weight: 400; }
</style>
</head>
<body>
<svg class="cover" viewBox="0 0 985 680" preserveAspectRatio="none" xmlns="http://www.w3.org/2000/svg" role="img" aria-label="Book cover: back, spine and front">

  <!-- Back cover -->
  <g class="back-cover">
    <g class="imprint-mark">
      <text class="imprint" x="447" y="58" text-anchor="end">Halvard Press</text>
      <circle cx="459" cy="54" r="4" fill="none" stroke="var(--gold)" stroke-width="1"/>
    </g>

    <g class="row-markers">
      <circle class="marker-outline" cx="41" cy="133" r="3"/>
      <circle class="marker-outline" cx="41" cy="247" r="3"/>
      <circle class="marker-outline" cx="41" cy="358" r="3"/>
      <circle class="marker-outline" cx="41" cy="471" r="3"/>
      <circle class="marker-outline" cx="41" cy="584" r="3"/>
    </g>

    <line class="rule-grey" x1="68" y1="255" x2="470" y2="255"/>
    <line class="rule-grey" x1="68" y1="371" x2="470" y2="371"/>
    <line class="rule-grey" x1="68" y1="485" x2="470" y2="485"/>
    <line class="rule-gold" x1="68" y1="596" x2="470" y2="596"/>
    <line class="rule-gold" x1="68" y1="145" x2="470" y2="572"/>

    <text class="back-author" x="280" y="618" text-anchor="middle">Tomas Brielink</text>
  </g>

  <!-- Spine -->
  <g class="spine">
    <text class="spine-author" transform="translate(488,40) rotate(90)">Tomas Brielink</text>
    <text class="spine-title" transform="translate(488,118) rotate(90)">Lanterns over Quiet Harbors and Orchards</text>
    <text class="imprint-small" transform="translate(487,636) rotate(90)">Halvard</text>
  </g>

  <!-- Front cover -->
  <g class="front-cover">
    <text class="front-title">
      <tspan x="541" y="56">Lanterns</tspan>
      <tspan x="541" y="86">over</tspan>
      <tspan x="541" y="116">Quiet</tspan>
      <tspan x="541" y="146">Harbors</tspan>
      <tspan x="541" y="176">and</tspan>
      <tspan x="541" y="206">Orchards</tspan>
    </text>

    <line class="rule-grey" x1="517" y1="246" x2="927" y2="145"/>
    <line class="rule-grey" x1="517" y1="364" x2="927" y2="264"/>
    <line class="rule-grey" x1="517" y1="477" x2="927" y2="377"/>
    <line class="rule-grey" x1="517" y1="588" x2="927" y2="489"/>
    <line class="rule-grey" x1="517" y1="596" x2="927" y2="596"/>

    <g class="row-markers">
      <rect class="marker-solid" x="948" y="129" width="8" height="8"/>
      <rect class="marker-solid" x="948" y="243" width="8" height="8"/>
      <rect class="marker-solid" x="948" y="354" width="8" height="8"/>
      <rect class="marker-solid" x="948" y="467" width="8" height="8"/>
      <rect class="marker-solid" x="948" y="580" width="8" height="8"/>
    </g>

    <text class="front-author" x="517" y="618">Tomas Brielink</text>
  </g>

  <!-- Bottom band -->
  <g class="bottom-band">
    <line class="rule-gold" x1="0" y1="630" x2="985" y2="630"/>
    <line class="rule-gold" x1="0" y1="632" x2="58" y2="680"/>
    <line class="rule-gold" x1="985" y1="632" x2="922" y2="680"/>
    <text class="band-title" x="68" y="655">Lanterns over Quiet Harbors and Orchards</text>
  </g>
</svg>
</body>
</html>
```